Schönheitssalon benötigt Flyer
Sehr schöne Arbeit, perfekt den Kundengeschmack getroffen. Leider zusätzliche Kosten durch (nicht enthaltene) Stockphotos, aber der Flyer ist sehr schick.
Zielgruppe
Ein Schönheitssalon in einer Pafümerie bietet diverse Angebote im Paket an (Gesichtsreinigung, Massage, Peeling, Maniküre, Sugaring). Vorrangig sollen Frauen angesprochen werden.
Aufgabenstellung
Faltblatt, gefalzt auf DIN A6 , 4-seiter
Endformat: 21,0 cm x 14,85 cm
gefalztes Endformat: 10,5 cm x 14,85 cm
Wir wünschen uns eine freundliche und helle Gestaltung mit rosé, voilett, pastell.
Das Grau, was jetzt gerade hinter dem Logo ist, wirkt sehr altbacken und nicht zeitgemäß.

```html
<!DOCTYPE html>
<html lang="de">
<head>
<meta charset="utf-8">
<title>Rosenstunde – Faltblatt</title>
<link href="https://fonts.googleapis.com/css2?family=Quicksand:wght@400;500;600;700&family=Great+Vibes&display=swap" rel="stylesheet">
<style>
:root{
  --page:#f7eef4;
  --paper:#fbe9f3;
  --paper-deep:#f3cfe4;
  --rose:#e0579c;
  --rose-soft:#ee8cbd;
  --rose-pale:#f4b7d6;
  --band:#f2b6d5;
  --ink:#8a8090;
  --white:#ffffff;
}
*{margin:0;padding:0;box-sizing:border-box}
html,body{width:1200px;height:3600px;overflow:hidden}
body{background:var(--page);font-family:"Quicksand",sans-serif;color:var(--ink);position:relative}
.spread{position:absolute;left:40px;width:1120px;height:792px;background:linear-gradient(135deg,#fdf3f9 0%,var(--paper) 55%,var(--paper-deep) 100%);overflow:hidden;box-shadow:0 6px 18px rgba(150,90,130,.18)}
.spread--outside{top:60px}
.spread--inside{top:920px}

/* outside */
.intro{position:absolute;left:40px;width:480px;top:100px;text-align:center;color:var(--rose);font-size:18px;line-height:1.45;font-weight:500}
.intro p{margin-bottom:26px}
.intro strong{font-weight:700}
.portrait{position:absolute;left:200px;top:420px;width:140px;height:140px;border-radius:50%;background:radial-gradient(circle at 50% 40%,#fff 0%,#f1e6e6 60%,#d9c8c4 100%);border:5px solid var(--white)}
.contact{position:absolute;left:40px;width:480px;top:590px;text-align:center;color:var(--rose);font-size:17px;line-height:1.35;font-weight:500}
.contact .hours{margin-top:20px}
.brand{position:absolute;left:820px;top:110px;width:260px;text-align:center;color:var(--rose);font-weight:500;font-size:40px;line-height:1.05}
.brand-dot{display:block;width:22px;height:22px;border-radius:50%;background:var(--rose-pale);margin:0 auto 10px}
.tagline{position:absolute;left:760px;top:240px;font-family:"Great Vibes",cursive;font-size:40px;color:var(--rose-pale)}
.face{position:absolute;left:0;top:0;width:1120px;height:792px}
.location{position:absolute;right:40px;top:720px;text-align:right;color:var(--rose);font-size:17px;line-height:1.3;font-weight:500}

/* inside */
.col-head{position:absolute;top:62px;color:var(--rose);font-size:22px;font-weight:600;letter-spacing:.12em}
.col-head--left{left:52px}
.col-head--right{left:578px}
.treatments{position:absolute;left:52px;top:110px;width:480px}
.treatment{margin-bottom:18px}
.treatment-line{display:flex;justify-content:space-between;color:var(--rose-soft);font-size:16px}
.treatment-line .meta{width:150px;display:flex;justify-content:space-between}
.treatment-desc{font-size:12.5px;line-height:1.4;color:var(--ink)}
.price-table{position:absolute;left:578px;top:100px;width:500px;border-collapse:collapse;font-size:13.5px}
.price-table th{color:var(--rose-soft);font-weight:500;font-size:12.5px;text-align:right;padding-bottom:4px}
.price-table td{padding:1px 0;line-height:1.3}
.price-table td.num{text-align:right;color:var(--rose-soft);width:65px}
.sugar{top:405px}
.sugar-table{top:445px;width:310px}
.band{position:absolute;left:0;bottom:0;width:1120px;height:792px}
.band-text{position:absolute;left:52px;bottom:26px;color:var(--white);font-size:14px;font-weight:700;letter-spacing:.14em}
</style>
</head>
<body>

<section class="spread spread--outside" aria-label="Außenseite">
  <div class="intro">
    <p>Erleben Sie eine Auszeit und schalten<br>Sie einfach mal ab bei einer<br>Wohlfühl-Gesichtsbehandlung.</p>
    <p><strong>Ich biete Ihnen auf Sie zugeschnittene<br>Kosmetikprogramme auf höchstem Niveau<br>mit hochwertigen Produkten.</strong></p>
    <p>Sie brauchen einfach nur genießen!<br>Ich freue mich auf Sie!</p>
  </div>
  <div class="portrait" role="img" aria-label="Porträtfoto der Kosmetikerin"></div>
  <div class="contact">
    <p>Musterstraße 120 a<br>12345 Musterstadt</p>
    <p class="hours">Öffnungszeiten<br>Do.: 9.30 – 19.00 Uhr<br>Fr.: 9.30 – 19.00 Uhr</p>
  </div>

  <div class="brand"><span class="brand-dot"></span>Rosenstunde</div>
  <div class="tagline">Entspannung &amp; Kosmetik</div>

  <svg class="face" viewBox="0 0 1120 792" role="img" aria-label="Foto einer Frau mit rosa Make-up">
    <defs>
      <linearGradient id="skin" x1="0" y1="0" x2="1" y2="1">
        <stop offset="0" stop-color="#f6e2da"/>
        <stop offset=".5" stop-color="#efd1c6"/>
        <stop offset="1" stop-color="#c9a28f"/>
      </linearGradient>
    </defs>
    <path d="M1120 330 L770 330 C650 360 590 470 600 600 C610 700 660 760 700 792 L1120 792 Z" fill="url(#skin)"/>
    <path d="M1080 420 A60 60 0 0 1 1080 520" fill="none" stroke="#fff" stroke-width="5"/>
  </svg>
  <p class="location">Im Haus der Stadt-<br>Parfümerie Lindqvist</p>
</section>

<section class="spread spread--inside" aria-label="Innenseite">
  <h2 class="col-head col-head--left">GESICHTSBEHANDLUNGEN</h2>
  <div class="treatments">
    <div class="treatment"><div class="treatment-line"><span>Reinigungs-Behandlung</span><span class="meta"><span>ca. 60 Min.</span><span>35,- €</span></span></div><p class="treatment-desc">Reinigung, Peeling, Ausreinigung, Maske &amp; Abschlusspflege</p></div>
    <div class="treatment"><div class="treatment-line"><span>Basis-Behandlung</span><span class="meta"><span>ca. 90 Min.</span><span>49,- €</span></span></div><p class="treatment-desc">Reinigung, Peeling, Ausreinigung, Augenbrauen-Korrektur,<br>Massage &amp; Maske, leichtes Make-Up auf Wunsch</p></div>
    <div class="treatment"><div class="treatment-line"><span>Intensiv-Behandlung</span><span class="meta"><span>ca. 90 Min.</span><span>59,- €</span></span></div><p class="treatment-desc">Reinigung, Peeling, Ausreinigung, Augenbrauen-Korrektur,<br>Ampulle, Massage, Maske &amp; Augenmaske, leichtes Make-Up<br>auf Wunsch</p></div>
    <div class="treatment"><div class="treatment-line"><span>Verwöhn-Behandlung</span><span class="meta"><span>ca. 90 Min.</span><span>67,- €</span></span></div><p class="treatment-desc">Reinigung, Peeling, Ausreinigung, Augenbrauen-Korrektur, Ampulle,<br>Massage, Maske, Hals- &amp; Dekolleté-Behandlung, leichtes Make-Up<br>auf Wunsch</p></div>
    <div class="treatment"><div class="treatment-line"><span>Luxus-Behandlung</span><span class="meta"><span>ca. 120 Min.</span><span>81,- €</span></span></div><p class="treatment-desc">Reinigung, Peeling, Ausreinigung, Augenbrauen-Korrektur,<br>Ampulle, Massage, Vlies-Maske, Augenmaske, Lippenpackung,<br>Handmassage &amp; Hals- &amp; Dekolleté-Behandlung,<br>leichtes Make-Up auf Wunsch</p></div>
    <div class="treatment"><div class="treatment-line"><span>Teenie-Behandlung (bis 18 Jahre)</span><span class="meta"><span>ca. 60 Min.</span><span>28,- €</span></span></div><p class="treatment-desc">Reinigung, Peeling, Ausreinigung &amp; Maske</p></div>
  </div>

  <h2 class="col-head col-head--right">ZUSATZ- &amp; EINZELBEHANDLUNGEN</h2>
  <table class="price-table">
    <tr><th></th><th>zusätzlich</th><th>einzeln</th></tr>
    <tr><td>Augenbrauen zupfen/wachsen</td><td class="num"></td><td class="num">8,- €</td></tr>
    <tr><td>Augenbrauen färben</td><td class="num">6,50 €</td><td class="num">8,50 €</td></tr>
    <tr><td>Wimpern färben</td><td class="num">7,- €</td><td class="num">9,- €</td></tr>
    <tr><td>Augenbrauen &amp; Wimpern färben + zupfen</td><td class="num"></td><td class="num">21,- €</td></tr>
    <tr><td>Wimpernwelle</td><td class="num">22,- €</td><td class="num">32,- €</td></tr>
    <tr><td>Pflegende Maniküre (60 Min.)</td><td class="num">18,- €</td><td class="num">26,- €</td></tr>
    <tr><td>Pflegende Maniküre + Lack</td><td class="num">24,- €</td><td class="num">32,- €</td></tr>
    <tr><td>Wirkstoffampulle</td><td class="num"></td><td class="num">9,- €</td></tr>
    <tr><td>Tages-Make-Up</td><td class="num"></td><td class="num">25,- €</td></tr>
    <tr><td>Abend- / Foto-Make-Up</td><td class="num"></td><td class="num">35,- €</td></tr>
    <tr><td>Braut-Make-Up (inkl. Probe)</td><td class="num"></td><td class="num">70,- €</td></tr>
    <tr><td>Klassische Rückenmassage ca. 30 Min.</td><td class="num"></td><td class="num">25,- €</td></tr>
  </table>

  <h2 class="col-head col-head--right sugar">SUGARING</h2>
  <table class="price-table sugar-table">
    <tr><td>Oberlippe</td><td class="num">9,- €</td></tr>
    <tr><td>Oberlippe + Kinn</td><td class="num">14,- €</td></tr>
    <tr><td>Arme</td><td class="num">ab 25,- €</td></tr>
    <tr><td>Beine Unterschenkel</td><td class="num">23,- €</td></tr>
    <tr><td>Beine komplett</td><td class="num">39,- €</td></tr>
    <tr><td>Rücken</td><td class="num">ab 35,- €</td></tr>
  </table>

  <svg class="band" viewBox="0 0 1120 792" aria-hidden="true">
    <path d="M0 712 C300 690 520 740 760 700 L760 792 L0 792 Z" fill="var(--band)"/>
  </svg>
  <svg class="band" viewBox="0 0 1120 792" role="img" aria-label="Foto einer entspannt liegenden Frau mit geschlossenen Augen">
    <defs>
      <linearGradient id="rest" x1="0" y1="0" x2="1" y2="0">
        <stop offset="0" stop-color="#f7d8e6"/>
        <stop offset=".6" stop-color="#efd0c8"/>
        <stop offset="1" stop-color="#d9b3a6"/>
      </linearGradient>
    </defs>
    <path d="M760 792 C770 700 860 620 1120 590 L1120 792 Z" fill="url(#rest)"/>
  </svg>
  <p class="band-text">ANDERE BEREICHE AUF ANFRAGE!</p>
</section>

</body>
</html>
```